Property Report

8 page document, similar theme to our website (www.harbourandmeadows.com) and previous brochure (provided). All content provided. We want a professional looking document. We need ASAP. Thanks!

Industry/Entity Type

Property

Font styles to use
Serif
Sans Serif

Colors
ffc214
ffcf3e
fee18a
fff3d1

Requirements
Must have
• Page 1: Cover
Page 2: Content
Page 3: About Us
Page 4: Site Description
Page 5: Scheme
Page 6: Analysis
Page 7: Conclusion
Page 8: Contact Details

```html
<!DOCTYPE html>
<html lang="en">
<head>
<meta charset="utf-8">
<title>Harbour &amp; Meadows Commercial – Contact Details</title>
<link rel="stylesheet" href="https://fonts.googleapis.com/css2?family=Montserrat:wght@300;400;700&display=swap">
<style>
  :root {
    --amber: #f6a922;
    --amber-veil: rgba(246, 169, 34, 0.82);
    --ink: #111111;
    --paper: #ffffff;
    --sky: #a3a8aa;
    --haze: #9a9fa1;
    --brick: #7d8183;
    --shadow: #646869;
    --road: #6d7173;
    --muted: #58595b;
    --frame: #000000;
  }
  * { margin: 0; padding: 0; box-sizing: border-box; }
  html, body { width: 848px; height: 1200px; overflow: hidden; background: var(--paper); }
  body { font-family: "Montserrat", Arial, sans-serif; color: var(--ink); }

  .page { position: relative; width: 848px; height: 1200px; background: var(--paper); }

  .hero-photo {
    position: absolute; left: 0; top: 0; width: 848px; height: 625px;
    background:
      radial-gradient(ellipse 360px 240px at 400px 360px, rgba(100, 104, 105, 0.55), rgba(100, 104, 105, 0) 100%),
      radial-gradient(ellipse 260px 320px at 80px 380px, rgba(90, 94, 96, 0.45), rgba(90, 94, 96, 0) 100%),
      radial-gradient(ellipse 220px 260px at 760px 380px, rgba(140, 145, 147, 0.5), rgba(140, 145, 147, 0) 100%),
      linear-gradient(180deg, var(--sky) 0%, var(--haze) 25%, var(--brick) 52%, var(--shadow) 80%, var(--road) 100%);
  }

  .brand-name {
    position: absolute; left: 0; top: 226px; width: 848px;
    text-align: center; color: var(--paper); font-weight: 700; letter-spacing: -1px;
  }
  .brand-name .line-one { display: block; font-size: 56px; line-height: 64px; }
  .brand-name .line-two { display: block; font-size: 72px; line-height: 74px; }
  .brand-name .line-three { display: block; font-size: 38px; line-height: 46px; letter-spacing: 0; }

  .page-frame {
    position: absolute; left: 50px; top: 50px; width: 749px; height: 1100px;
    border: 2px solid var(--frame); pointer-events: none;
  }

  .contact-card-veil {
    position: absolute; left: 141px; top: 592px; width: 566px; height: 33px;
    background: var(--amber-veil);
  }
  .contact-card {
    position: absolute; left: 141px; top: 625px; width: 566px; height: 227px;
    background: var(--amber); text-align: center;
  }
  .contact-card .company {
    margin-top: 36px; color: var(--paper);
    font-weight: 700; font-size: 26px; line-height: 32px;
  }
  .contact-card .address {
    margin-top: 8px; font-weight: 400; font-size: 20px; line-height: 25px; letter-spacing: 0.4px;
  }
  .contact-card .phone {
    margin-top: 15px; font-weight: 700; font-size: 20px; line-height: 26px;
  }
  .contact-card .email {
    margin-top: 5px; font-weight: 700; font-size: 20px; line-height: 26px;
  }

  .website {
    position: absolute; left: 0; top: 1085px; width: 848px; text-align: center;
    color: var(--muted); font-weight: 400; font-size: 24px; letter-spacing: 0.3px;
  }
</style>
</head>
<body>
  <main class="page">
    <div class="hero-photo" role="img" aria-label="Grey-toned street photograph of a modern four-storey brick office building on a corner, with bare trees, pedestrians and a road in the foreground"></div>

    <div class="brand-name">
      <span class="line-one">Harbour &amp;</span>
      <span class="line-two">Meadows</span>
      <span class="line-three">Commercial</span>
    </div>

    <div class="contact-card-veil"></div>
    <section class="contact-card">
      <h1 class="company">Harbour &amp; Meadows Commercial</h1>
      <p class="address">Unit 4, 18 Larkfield Road<br>London SE9 4QT</p>
      <p class="phone">020 7946 0321</p>
      <p class="email">info@harbourandmeadows.com</p>
    </section>

    <p class="website">www.harbourandmeadows.com</p>

    <div class="page-frame"></div>
  </main>
</body>
</html>
```